Business Card Design Project

We have a logo design and are now looking for a business card design. We supply pre-construction services to the Wireless Telecommunication Industry in the development of cell phone tower and other antenna supporting infrastructure e.g. buildings. The types of services include Real Estate Leasing, Zoning & Permitting,Surveying and A&E work. I am looking for a card that includes the logo we have selected along with the full company name. Company colors are Blue and Silver. I want something professional and that "pops". Use your imagination with the four sided star portion of the logo - it can be stretched such that it occupies a large portion of the card or kept simple the way it is. I am interested in seeing the design on a white, silver, navy, black or charcoal background or any other color you think works well with the logo. Apart from the logo that includes HRM we also need to see the full company name on the card - Harborline Relay Maintenance, Inc. The design must also show a persons name, title, address, (2) phone numbers, e-mail address and web address www.hrm.example

Target Market(s)

Cell phone carriers e.g. Quellport Mobile, BN&K, Zandex Cell, Ovalo etc.

Industry/Entity Type

Cell Phone

Requirements
Must have
• Logo and
Harborline Relay Maintenance, Inc.

```html
<!DOCTYPE html>
<html lang="en">
<head>
<meta charset="utf-8">
<title>HRM Business Card Concepts</title>
<link rel="stylesheet" href="https://fonts.googleapis.com/css2?family=PT+Sans+Narrow:wght@700&family=Source+Sans+3:wght@400;600;700&display=swap">
<style>
  :root {
    --page: #ffffff;
    --ink: #1d1d1b;
    --accent: #3a8ad0;
    --charcoal: #2a2628;
    --teal-navy: #063646;
    --text-light: #9cc8ea;
    --rule-blue: #2d88d2;
    --logo-blue: #2f8fd8;
    --crop: #c9c9c9;
  }
  html, body {
    margin: 0;
    width: 1200px;
    height: 900px;
    overflow: hidden;
    background: var(--page);
  }
  .sheet {
    position: relative;
    width: 1200px;
    height: 900px;
  }
  .headline {
    position: absolute;
    left: 274px;
    top: 124px;
    margin: 0;
    font-family: "Source Sans 3", sans-serif;
    font-weight: 400;
    font-size: 54px;
    line-height: 50px;
    letter-spacing: -0.5px;
    color: var(--ink);
    white-space: nowrap;
  }
  .headline .highlight {
    font-family: "PT Sans Narrow", sans-serif;
    font-weight: 700;
    color: var(--accent);
    font-size: 50px;
  }
  .crop-marks {
    position: absolute;
    left: 0;
    top: 0;
  }
  .card {
    position: absolute;
    overflow: hidden;
    font-family: "Source Sans 3", sans-serif;
    color: var(--text-light);
  }
  .card--charcoal { background: var(--charcoal); }
  .card--navy { background: var(--teal-navy); }
  .card-1 { left: 275px; top: 247px; width: 343px; height: 223px; }
  .card-2 { left: 618px; top: 247px; width: 344px; height: 223px; }
  .card-3 { left: 275px; top: 470px; width: 343px; height: 222px; }
  .card-4 { left: 618px; top: 470px; width: 344px; height: 222px; }

  .decor { position: absolute; }
  .logo {
    position: absolute;
    display: flex;
    align-items: center;
    gap: 8px;
    font-weight: 700;
    color: var(--logo-blue);
    letter-spacing: 1px;
    line-height: 1;
  }
  .logo-dot {
    display: inline-block;
    border-radius: 50%;
    background: var(--logo-blue);
  }
  .company {
    position: absolute;
    font-size: 10px;
    line-height: 12px;
    letter-spacing: 0.4px;
    white-space: nowrap;
    color: var(--text-light);
  }
  .company--centered { transform: translateX(-50%); }
  .details {
    position: absolute;
    text-align: center;
    width: 260px;
    transform: translateX(-50%);
  }
  .details .title,
  .details .name {
    display: block;
    font-size: 15px;
    line-height: 14px;
  }
  .details .rule {
    display: block;
    height: 2px;
    background: var(--rule-blue);
    margin: 4px auto 3px;
  }
  .details .contact {
    display: block;
    font-size: 12px;
    line-height: 12.5px;
  }
  .details--roomy .contact {
    font-size: 13px;
    line-height: 15px;
  }
</style>
</head>
<body>
<main class="sheet">
  <h1 class="headline">IF YOU WANT TO MAKE BETTER<br>TAKE <span class="highlight">ME THE JOB</span></h1>

  <svg class="crop-marks" width="1200" height="900" aria-hidden="true">
    <g stroke="var(--crop)" stroke-width="1">
      <line x1="275" y1="222" x2="275" y2="240"/>
      <line x1="618" y1="222" x2="618" y2="240"/>
      <line x1="962" y1="222" x2="962" y2="240"/>
      <line x1="275" y1="698" x2="275" y2="716"/>
      <line x1="618" y1="698" x2="618" y2="716"/>
      <line x1="962" y1="698" x2="962" y2="724"/>
      <line x1="248" y1="247" x2="268" y2="247"/>
      <line x1="248" y1="470" x2="268" y2="470"/>
      <line x1="248" y1="692" x2="268" y2="692"/>
      <line x1="968" y1="247" x2="988" y2="247"/>
      <line x1="968" y1="470" x2="988" y2="470"/>
      <line x1="968" y1="692" x2="988" y2="692"/>
    </g>
  </svg>

  <!-- Card 1: charcoal, small mark -->
  <section class="card card--charcoal card-1">
    <div class="decor" role="img" aria-label="Faint silver sweeping star decoration" style="left:0;top:0;width:343px;height:223px;background:radial-gradient(ellipse at 45% 45%, rgba(150,150,150,0.18), rgba(0,0,0,0) 65%);"></div>
    <div class="logo" style="left:102px;top:20px;font-size:36px;">HRM<span class="logo-dot" style="width:14px;height:14px;"></span></div>
    <div class="company company--centered" style="left:150px;top:62px;">Harborline Relay Maintenance, Inc.</div>
    <div class="details" style="left:172px;top:123px;">
      <span class="title">graphics designer</span>
      <span class="name">Teodor Vallin</span>
      <span class="rule" style="width:186px;"></span>
      <span class="contact">(1)ph. 5550147236</span>
      <span class="contact">(2)ph. 5550142345</span>
      <span class="contact">e-mail: teodor@mailbox.example</span>
      <span class="contact">www.hrm.example</span>
    </div>
  </section>

  <!-- Card 2: navy, large mark -->
  <section class="card card--navy card-2">
    <div class="decor" role="img" aria-label="Soft glow behind the large mark" style="left:0;top:60px;width:160px;height:160px;background:radial-gradient(circle at 40% 60%, rgba(70,140,190,0.25), rgba(0,0,0,0) 60%);"></div>
    <div class="company" style="right:16px;top:6px;">Harborline Relay Maintenance, Inc.</div>
    <div class="logo" style="left:38px;top:14px;font-size:110px;letter-spacing:6px;">HRM</div>
    <div class="details details--roomy" style="left:170px;top:124px;">
      <span class="title">graphics designer</span>
      <span class="name">Teodor Vallin</span>
      <span class="rule" style="width:142px;"></span>
      <span class="contact">(1)ph. 5550147236</span>
      <span class="contact">(2)ph. 5550142345</span>
      <span class="contact">e-mail: teodor@mailbox.example</span>
      <span class="contact">www.hrm.example</span>
    </div>
  </section>

  <!-- Card 3: charcoal, medium mark -->
  <section class="card card--charcoal card-3">
    <div class="decor" role="img" aria-label="Faint grey cross-shaped star decoration" style="left:0;top:0;width:180px;height:222px;background:linear-gradient(90deg, rgba(110,110,110,0.22), rgba(0,0,0,0));"></div>
    <div class="logo" style="left:52px;top:48px;font-size:50px;">HRM<span class="logo-dot" style="width:18px;height:18px;"></span></div>
    <div class="company company--centered" style="left:126px;top:100px;">Harborline Relay Maintenance, Inc.</div>
    <div class="details" style="left:171px;top:128px;">
      <span class="title">graphics designer</span>
      <span class="name">Teodor Vallin</span>
      <span class="rule" style="width:255px;"></span>
      <span class="contact">(1)ph. 5550147236</span>
      <span class="contact">(2)ph. 5550142345</span>
      <span class="contact">e-mail: teodor@mailbox.example</span>
      <span class="contact">www.hrm.example</span>
    </div>
  </section>

  <!-- Card 4: navy, mark right of dot -->
  <section class="card card--navy card-4">
    <div class="decor" role="img" aria-label="Faint cross-shaped star decoration" style="left:190px;top:0;width:154px;height:222px;background:linear-gradient(270deg, rgba(60,110,140,0.3), rgba(0,0,0,0));"></div>
    <div class="logo" style="left:88px;top:22px;font-size:44px;"><span class="logo-dot" style="width:18px;height:18px;"></span>HRM</div>
    <div class="company company--centered" style="left:170px;top:66px;">Harborline Relay Maintenance, Inc.</div>
    <div class="details details--roomy" style="left:170px;top:82px;">
      <span class="title">graphics designer</span>
      <span class="name">Teodor Vallin</span>
      <span class="rule" style="width:142px;"></span>
      <span class="contact">(1)ph. 5550147236</span>
      <span class="contact">(2)ph. 5550142345</span>
      <span class="contact">e-mail: teodor@mailbox.example</span>
      <span class="contact">www.hrm.example</span>
    </div>
  </section>
</main>
</body>
</html>
```